Job site for brightlarkyard.com

Update: Looking for a really simple design that is fit for a short attention span.
Need a website built that I can host on Zentrovo.com.
Need tracking: Important to track where students are clicking and be able to provide that detail to employers.
The site will use the brightlarkyard.com logo (attached).
Add a tagline - Highschool Students Start Here
( Link on main page) Job Opportunities (click to page)
- Listing of new jobs.
o Job Title
o Company Name
o Position Description
o Hyperlink to employer website (need to be able to track clicks)
(Link on main page) Tools & Career Advice (click to page)
o This section would allow for the posting of advice and articles.
(Link on main page) Ask a Job Question? (click to page)
o Submit a question via email – email only collected. No personal
info.
(Link on main page) Volunteer Opportunities (click to page)
o A listing of organizations that need student volunteers. Need
to be able to add a new listing. Similar to a job listing:
Business or Non-profit Name
Description of need
Hyperlink to website or simply contact info.
(Link on main page) About Us
- Be able to change the content
Updates
Gathering more feedback
Target Market(s)
Ages 14-18
Industry/Entity Type
job board
Coding
Coded - Design and coding required
Number of Pages Required
4 page

```html
<!DOCTYPE html>
<html lang="en">
<head>
<meta charset="utf-8">
<title>brightlarkyard.com – Highschool Students Start Here</title>
<link href="https://fonts.googleapis.com/css2?family=Roboto:wght@400;500;700;900&display=swap" rel="stylesheet">
<style>
:root{
  --blue:#1ba6dc;
  --blue-dark:#1590c2;
  --orange:#f7811e;
  --ink:#1d1f22;
  --text:#2b2e33;
  --muted:#9a9ea4;
  --tint:#eef8fd;
  --footer:#0b0b0c;
  --line:#e4e6e9;
}
*{margin:0;padding:0;box-sizing:border-box}
html,body{width:1200px;height:3999px;overflow:hidden}
body{position:relative;background:#fff;font-family:"Roboto",Arial,sans-serif;color:var(--text)}
.abs{position:absolute}
a{color:inherit;text-decoration:none}

/* header */
.topline{left:0;top:0;width:1200px;height:4px;background:var(--blue)}
.brand{left:62px;top:50px;display:flex;align-items:center;gap:7px;white-space:nowrap}
.brand-dot{width:14px;height:14px;border-radius:50%;background:var(--blue);flex:none}
.brand-name{font-size:15px;font-weight:500;color:var(--blue)}
.nav{left:236px;top:52px;display:flex;gap:23px;font-size:13.5px;color:var(--ink);text-transform:uppercase}
.search{left:1097px;top:53px}

/* hero */
.hero{left:0;top:124px;width:1200px;height:696px}
.hero-title{left:0;top:378px;width:1200px;text-align:center;color:#fff;font-weight:900;font-size:53px;line-height:50px;letter-spacing:.5px}
.hero-text{left:0;top:493px;width:1200px;text-align:center;color:#fff;font-size:15px;line-height:26px}
.btn{display:inline-flex;align-items:center;gap:10px;color:#fff;font-weight:700;text-transform:uppercase;font-size:15px;border-radius:3px;padding:0 17px;height:42px;background:var(--blue)}
.btn-orange{left:514px;top:562px;height:47px;background:var(--orange)}
.slide-arrow{width:38px;height:38px;border-radius:50%;background:#fff;top:479px;display:flex;align-items:center;justify-content:center}

/* section headings */
.sec-title{left:0;width:1200px;text-align:center;font-size:40px;font-weight:700;color:var(--ink);letter-spacing:.5px}
.sec-rule{left:571px;width:59px;height:3px;background:var(--blue)}

/* job cards */
.card{width:289px;height:315px;background:#fff;box-shadow:0 0 6px rgba(0,0,0,.15)}
.card .icon{position:absolute;left:18px;top:31px;width:70px;height:70px;background:var(--blue);border-radius:6px}
.card h3{position:absolute;left:18px;top:117px;font-size:14.5px;font-weight:700;color:var(--ink);text-transform:uppercase}
.card .co{position:absolute;left:18px;top:148px;font-size:13.5px;color:var(--muted)}
.card p{position:absolute;left:18px;top:170px;width:260px;font-size:15px;line-height:26px;color:var(--text)}
.card .btn{position:absolute;left:17px;top:242px}

/* about */
.about-bg{left:0;top:1397px;width:1200px;height:536px;background:var(--tint)}
.owl-art{left:137px;top:1459px;width:357px;height:412px;border-radius:50% 50% 44% 44%;background:linear-gradient(180deg,#2a3440 0%,#26303a 60%,#1ba6dc 100%)}
.about-title{left:568px;top:1470px;font-size:40px;font-weight:700;color:var(--ink)}
.about-text{left:568px;top:1544px;width:500px;font-size:15px;line-height:25.8px;color:var(--text)}

/* articles */
.post{background:#fff;box-shadow:0 0 6px rgba(0,0,0,.13)}
.photo{position:absolute}
.date{position:absolute;width:53px;height:47px;background:var(--blue);color:#fff;text-align:center;font-weight:700;line-height:19px;padding-top:4px}
.date b{display:block;font-size:21px}
.date span{font-size:14px}
.meta{position:absolute;display:flex;gap:16px;font-size:14px;color:var(--blue);align-items:center}
.meta i{display:inline-flex;align-items:center;gap:6px;font-style:normal}
.post h4{position:absolute;font-size:14px;font-weight:700;color:var(--ink);text-transform:uppercase;line-height:20px}
.post p{position:absolute;color:var(--muted)}
.more{position:absolute;display:flex;align-items:center;gap:8px;color:var(--blue);font-weight:700;font-size:14.5px}

/* ask */
.ask-bg{left:0;top:2628px;width:1200px;height:368px;background:var(--tint)}
.field{top:2797px;width:359px;height:38px;background:#fff;border:1px solid #cfd3d7;font-size:15px;color:var(--text);padding:9px 18px}
.btn-submit{left:531px;top:2870px;height:39px;padding:0 24px}

/* footer */
.footer{left:0;top:3560px;width:1200px;height:439px}
.f-head{top:3692px;font-size:14.5px;font-weight:700;color:#fff;text-decoration:underline;text-transform:uppercase}
.f-list{top:3733px;list-style:none;font-size:14px;color:#fff;line-height:34px}
.f-contact{left:849px;top:3733px;font-size:14px;color:#fff}
.f-row{display:flex;align-items:center;gap:14px;margin-bottom:20px;line-height:21px}
.f-ico{width:34px;height:34px;border-radius:50%;background:#fff;display:flex;align-items:center;justify-content:center;flex:none}
.f-brand{left:109px;top:3760px}
.f-brand .brand-name{font-size:19px}
.f-brand .brand-dot{width:20px;height:20px}
.f-about{left:109px;top:3826px;width:290px;font-size:14px;line-height:26px;color:#fff}
.f-rule{left:110px;top:3946px;width:969px;height:1px;background:#3a3c40}
.social{top:3968px;display:flex;gap:20px;left:110px}
.social span{width:14px;height:14px;border-radius:50%;background:#fff}
.copy{left:0;top:3965px;width:1200px;text-align:center;color:#fff;font-size:13.5px}
</style>
</head>
<body>

<!-- header -->
<div class="abs topline"></div>
<a class="abs brand" href="#"><span class="brand-dot"></span><span class="brand-name">brightlarkyard.com</span></a>
<nav class="abs nav">
  <a href="#">Home</a><a href="#">About Us</a><a href="#">Job Opportunities</a><a href="#">Tools &amp; Career Advice</a><a href="#">Ask a Job Question?</a><a href="#">Volunteer Opportunities</a>
</nav>
<svg class="abs search" width="16" height="16" viewBox="0 0 16 16"><circle cx="6.5" cy="6.5" r="4.8" fill="none" stroke="#1d1f22" stroke-width="2.2"/><line x1="10" y1="10" x2="14.5" y2="14.5" stroke="#1d1f22" stroke-width="2.6" stroke-linecap="round"/></svg>

<!-- hero -->
<svg class="abs hero" viewBox="0 0 1200 696" role="img" aria-label="Photo of smiling high school students working together at a table">
  <defs><linearGradient id="heroGrad" x1="0" y1="0" x2="1" y2="1"><stop offset="0" stop-color="#3d4a54"/><stop offset=".5" stop-color="#5b5a55"/><stop offset="1" stop-color="#2e3a42"/></linearGradient></defs>
  <polygon points="0,0 1200,0 1200,582 600,683 0,582" fill="url(#heroGrad)"/>
  <polygon points="0,582 600,683 1200,582 600,696" fill="#1ba6dc"/>
</svg>
<h1 class="abs hero-title">HIGHSCHOOL STUDENTS<br>START HERE</h1>
<p class="abs hero-text">Lorem ipsum dolor sit amet, consectetur adipiscing elit, sed do eiusmod tempor incididunt ut labore<br>et dolore magna aliqua. Ut enim ad minim veniam, quis nostrud exercitation.</p>
<a class="abs btn btn-orange" href="#">Get Started <svg width="16" height="16" viewBox="0 0 16 16"><circle cx="8" cy="8" r="8" fill="#fff"/><path d="M6.5 4.5 10 8 6.5 11.5" fill="none" stroke="#f7811e" stroke-width="2.2"/></svg></a>
<div class="abs slide-arrow" style="left:35px"><svg width="14" height="14" viewBox="0 0 14 14"><path d="M9 2 4 7l5 5" fill="none" stroke="#1d1f22" stroke-width="2"/></svg></div>
<div class="abs slide-arrow" style="left:1124px"><svg width="14" height="14" viewBox="0 0 14 14"><path d="M5 2l5 5-5 5" fill="none" stroke="#1d1f22" stroke-width="2"/></svg></div>

<!-- job opportunities -->
<h2 class="abs sec-title" style="top:897px">JOB OPPORTUNITIES</h2>
<div class="abs sec-rule" style="top:949px"></div>

<div class="abs card" style="left:129px;top:994px"><div class="icon" role="img" aria-label="Icon of a student at a computer desk"></div><h3>JPO Training</h3><div class="co">Northgate Works Ltd</div><p>Lorem ipsum dolor sit consectetur adipiscing elit, sed dodolor&nbsp; eiusmod</p><a class="btn" href="#">Click Here <svg width="16" height="16" viewBox="0 0 16 16"><circle cx="8" cy="8" r="8" fill="#fff"/><path d="M6.5 4.5 10 8 6.5 11.5" fill="none" stroke="#1ba6dc" stroke-width="2.2"/></svg></a></div>
<div class="abs card" style="left:455px;top:994px"><div class="icon" role="img" aria-label="Icon of a worker at a laptop"></div><h3 style="top:120px">JPO Training</h3><div class="co" style="top:151px">Northgate Works Ltd</div><p style="top:172px">Lorem ipsum dolor sit consectetur adipiscing elit, sed dodolor&nbsp; eiusmod</p><a class="btn" href="#">Click Here <svg width="16" height="16" viewBox="0 0 16 16"><circle cx="8" cy="8" r="8" fill="#fff"/><path d="M6.5 4.5 10 8 6.5 11.5" fill="none" stroke="#1ba6dc" stroke-width="2.2"/></svg></a></div>
<div class="abs card" style="left:781px;top:994px"><div class="icon" style="width:56px" role="img" aria-label="Icon of a graduate in a cap"></div><h3>JPO Training</h3><div class="co">Northgate Works Ltd</div><p>Lorem ipsum dolor sit consectetur adipiscing elit, sed dodolor&nbsp; eiusmod</p><a class="btn" href="#">Click Here <svg width="16" height="16" viewBox="0 0 16 16"><circle cx="8" cy="8" r="8" fill="#fff"/><path d="M6.5 4.5 10 8 6.5 11.5" fill="none" stroke="#1ba6dc" stroke-width="2.2"/></svg></a></div>

<!-- about -->
<div class="abs about-bg"></div>
<div class="abs owl-art" role="img" aria-label="Illustration of a mascot bird wearing a graduation cap"></div>
<h2 class="abs about-title">ABOUT US</h2>
<p class="abs about-text">Lorem ipsum dolor sit amet, consectetur adipiscing elit, sed do eiusmod tempor incididunt ut labore et dolore magna aliqua. Ut enim ad minim veniam, quis nostrud exercitation ullamco laboris nisi ut aliquip ex ea commodo consequat. Duis aute irure dolor in reprehenderit in voluptate velit esse cillum dolore eu fugiat nulla pariatur.Excepteur sint occaecat cupidatat non proident, sunt in culpa qui officia deserunt mollit anim id laborumSed ut perspiciatis&nbsp; omnis voluptatem accusantium doloremque laudantium, totam rem aperiam, eaque ipsa quae illo inventore veritatis et quasi architecto beatae vitae dicta sunt explicabo. Nemo enim ipsam</p>
<a class="abs btn" style="left:568px;top:1802px;height:48px" href="#">Learn More <svg width="16" height="16" viewBox="0 0 16 16"><circle cx="8" cy="8" r="8" fill="#fff"/><path d="M6.5 4.5 10 8 6.5 11.5" fill="none" stroke="#1ba6dc" stroke-width="2.2"/></svg></a>

<!-- tools & career advice -->
<h2 class="abs sec-title" style="top:2012px">TOOLS &amp; CAREER ADVICE</h2>
<div class="abs sec-rule" style="top:2064px"></div>

<article class="abs post" style="left:158px;top:2117px;width:359px;height:420px">
  <div class="photo" style="left:8px;top:8px;width:343px;height:171px;background:linear-gradient(135deg,#8a7a6a,#d8d2c8 50%,#6d7f8e)" role="img" aria-label="Photo of students studying together on laptops"></div>
  <div class="date" style="left:8px;top:8px"><b>13</b><span>Sep</span></div>
  <div class="meta" style="left:18px;top:207px"><i><svg width="14" height="14" viewBox="0 0 14 14"><rect x="1" y="2.5" width="12" height="10.5" rx="1" fill="none" stroke="#1ba6dc" stroke-width="1.4"/><line x1="1" y1="6" x2="13" y2="6" stroke="#1ba6dc" stroke-width="1.4"/></svg>Sep 13 ,2021</i><i><svg width="15" height="13" viewBox="0 0 15 13"><ellipse cx="7.5" cy="6" rx="6.5" ry="4.8" fill="none" stroke="#1ba6dc" stroke-width="1.3"/></svg>Comments</i></div>
  <h4 style="left:18px;top:240px;width:330px">Lorem ipsum dolor sit consectetur adipiscing elit, sed do eiusmod tempor</h4>
  <p style="left:18px;top:290px;width:330px;font-size:15px;line-height:25.5px">Sed ut perspiciatis unde omnis iste natus error sit voluptatem accusantium doloremque ltium, totam rem aperiam, eaque ipsa quae ab</p>
  <a class="more" style="left:18px;top:378px" href="#">READ MORE <svg width="14" height="14" viewBox="0 0 16 16"><circle cx="8" cy="8" r="8" fill="#1ba6dc"/><path d="M6.5 4.5 10 8 6.5 11.5" fill="none" stroke="#fff" stroke-width="2.2"/></svg></a>
</article>

<article class="abs post" style="left:550px;top:2117px;width:492px;height:202px">
  <div class="photo" style="left:9px;top:8px;width:169px;height:185px;background:linear-gradient(160deg,#b98f62,#5a8fa4 55%,#2f3b44)" role="img" aria-label="Photo of students gathered around a laptop"></div>
  <div class="date" style="left:9px;top:8px"><b>13</b><span>Sep</span></div>
  <h4 style="left:198px;top:21px">Sed ut perspiciatis unde omnis</h4>
  <div class="meta" style="left:198px;top:52px;font-size:13.5px"><i><svg width="13" height="13" viewBox="0 0 14 14"><rect x="1" y="2.5" width="12" height="10.5" rx="1" fill="none" stroke="#1ba6dc" stroke-width="1.4"/><line x1="1" y1="6" x2="13" y2="6" stroke="#1ba6dc" stroke-width="1.4"/></svg>Sep 13 ,2021</i><i><svg width="14" height="12" viewBox="0 0 15 13"><ellipse cx="7.5" cy="6" rx="6.5" ry="4.8" fill="none" stroke="#1ba6dc" stroke-width="1.3"/></svg>Comments</i></div>
  <p style="left:198px;top:81px;width:280px;font-size:13px;line-height:22.5px">Sed ut perspiciatis unde omnis iste natus error&nbsp; voluptatem accusantium doloremque laudantium, totam rem aperiam, eaque ipsa</p>
  <a class="more" style="left:198px;top:161px;font-size:14px" href="#">Read More <svg width="14" height="14" viewBox="0 0 16 16"><circle cx="8" cy="8" r="8" fill="#1ba6dc"/><path d="M6.5 4.5 10 8 6.5 11.5" fill="none" stroke="#fff" stroke-width="2.2"/></svg></a>
</article>

<article class="abs post" style="left:550px;top:2333px;width:492px;height:202px">
  <div class="photo" style="left:9px;top:8px;width:169px;height:185px;background:linear-gradient(160deg,#a9a39a,#c9a24c 55%,#3a4c5c)" role="img" aria-label="Photo of students holding books and folders"></div>
  <div class="date" style="left:9px;top:8px"><b>13</b><span>Sep</span></div>
  <h4 style="left:198px;top:21px">Sed ut perspiciatis unde omnis</h4>
  <div class="meta" style="left:198px;top:52px;font-size:13.5px"><i><svg width="13" height="13" viewBox="0 0 14 14"><rect x="1" y="2.5" width="12" height="10.5" rx="1" fill="none" stroke="#1ba6dc" stroke-width="1.4"/><line x1="1" y1="6" x2="13" y2="6" stroke="#1ba6dc" stroke-width="1.4"/></svg>Sep 13 ,2021</i><i><svg width="14" height="12" viewBox="0 0 15 13"><ellipse cx="7.5" cy="6" rx="6.5" ry="4.8" fill="none" stroke="#1ba6dc" stroke-width="1.3"/></svg>Comments</i></div>
  <p style="left:198px;top:81px;width:280px;font-size:13px;line-height:22.5px">Sed ut perspiciatis unde omnis iste natus error&nbsp; voluptatem accusantium doloremque laudantium, totam rem aperiam, eaque ipsa</p>
  <a class="more" style="left:198px;top:161px;font-size:14px" href="#">Read More <svg width="14" height="14" viewBox="0 0 16 16"><circle cx="8" cy="8" r="8" fill="#1ba6dc"/><path d="M6.5 4.5 10 8 6.5 11.5" fill="none" stroke="#fff" stroke-width="2.2"/></svg></a>
</article>

<!-- ask a job question -->
<div class="abs ask-bg"></div>
<h2 class="abs sec-title" style="top:2704px">ASK A JOB QUESTION?</h2>
<div class="abs sec-rule" style="top:2756px"></div>
<div class="abs field" style="left:236px">Email:</div>
<div class="abs field" style="left:604px">Ask a Job Question?:</div>
<a class="abs btn btn-submit" href="#">Submit <svg width="16" height="16" viewBox="0 0 16 16"><circle cx="8" cy="8" r="8" fill="#fff"/><path d="M6.5 4.5 10 8 6.5 11.5" fill="none" stroke="#1ba6dc" stroke-width="2.2"/></svg></a>

<!-- volunteer listings -->
<h2 class="abs sec-title" style="top:3077px">JOB OPPORTUNITIES</h2>
<div class="abs sec-rule" style="top:3129px"></div>

<div class="abs card" style="left:129px;top:3175px"><div class="icon" style="width:60px;top:35px;height:62px" role="img" aria-label="Icon of a person at a desk"></div><h3 style="top:114px">Perspiciatis unde</h3><div class="co" style="top:145px">Lorem ipsum dolor sit amet</div><p style="top:172px">Lorem ipsum dolor sit consectetur adipiscing elit, sed dodolor&nbsp; eiusmod</p><a class="btn" href="#">Contact Us <svg width="16" height="16" viewBox="0 0 16 16"><circle cx="8" cy="8" r="8" fill="#fff"/><path d="M6.5 4.5 10 8 6.5 11.5" fill="none" stroke="#1ba6dc" stroke-width="2.2"/></svg></a></div>
<div class="abs card" style="left:455px;top:3175px"><div class="icon" style="width:60px;top:33px" role="img" aria-label="Icon of a teacher at a board"></div><h3 style="top:117px">Perspiciatis unde</h3><div class="co" style="top:148px">Lorem ipsum dolor sit amet</div><p style="top:172px">Lorem ipsum dolor sit consectetur adipiscing elit, sed dodolor&nbsp; eiusmod</p><a class="btn" href="#">Contact Us <svg width="16" height="16" viewBox="0 0 16 16"><circle cx="8" cy="8" r="8" fill="#fff"/><path d="M6.5 4.5 10 8 6.5 11.5" fill="none" stroke="#1ba6dc" stroke-width="2.2"/></svg></a></div>
<div class="abs card" style="left:781px;top:3175px"><div class="icon" style="width:60px;top:28px;height:76px" role="img" aria-label="Icon of a person wearing a cap"></div><h3 style="top:121px">Perspiciatis unde</h3><div class="co" style="top:152px">Lorem ipsum dolor sit amet</div><p style="top:176px">Lorem ipsum dolor sit consectetur adipiscing elit, sed dodolor&nbsp; eiusmod</p><a class="btn" style="top:246px" href="#">Contact Us <svg width="16" height="16" viewBox="0 0 16 16"><circle cx="8" cy="8" r="8" fill="#fff"/><path d="M6.5 4.5 10 8 6.5 11.5" fill="none" stroke="#1ba6dc" stroke-width="2.2"/></svg></a></div>

<!-- footer -->
<svg class="abs footer" viewBox="0 0 1200 439" aria-hidden="true">
  <polygon points="0,127 600,11 1200,127" fill="#1ba6dc"/>
  <polygon points="0,127 600,27 1200,127 1200,439 0,439" fill="#0b0b0c"/>
</svg>
<a class="abs brand f-brand" href="#"><span class="brand-dot"></span><span class="brand-name">brightlarkyard.com</span></a>
<p class="abs f-about">Lorem ipsum dolor amet, consectetur adipiscing elit, sed do eiusmod tempor</p>

<div class="abs f-head" style="left:442px">Other Links</div>
<ul class="abs f-list" style="left:442px"><li>FAQ</li><li>Services</li><li>Privacy &amp; Policy</li><li>Team</li></ul>
<div class="abs f-head" style="left:621px">Quick Links</div>
<ul class="abs f-list" style="left:621px"><li>Home</li><li>About Us</li><li>Job Opportunities</li><li>Tools &amp; Career Advice</li><li>Ask a Job Question?</li><li>Volunteer Opportunities</li></ul>
<div class="abs f-head" style="left:849px">Contact Us</div>
<div class="abs f-contact">
  <div class="f-row"><span class="f-ico"><svg width="16" height="16" viewBox="0 0 16 16"><path d="M3 1.5l3 .5 1 3.5-2 1.2a9 9 0 0 0 4.3 4.3l1.2-2 3.5 1 .5 3c-1 1.5-3 1.6-5 .7A14 14 0 0 1 2.2 6.5C1.3 4.5 1.5 2.5 3 1.5z" fill="#111"/></svg></span>555-010-2858</div>
  <div class="f-row"><span class="f-ico"><svg width="16" height="13" viewBox="0 0 16 13"><rect x="1" y="1" width="14" height="11" rx="1.5" fill="none" stroke="#111" stroke-width="1.6"/><path d="M1.5 2 8 7l6.5-5" fill="none" stroke="#111" stroke-width="1.6"/></svg></span>info@brightlarkyard.com</div>
  <div class="f-row"><span class="f-ico"><svg width="14" height="18" viewBox="0 0 14 18"><path d="M7 17S1 10.5 1 6.5a6 6 0 0 1 12 0C13 10.5 7 17 7 17z" fill="#111"/><circle cx="7" cy="6.5" r="2.2" fill="#fff"/></svg></span>12, Lorem ipsum dolor amet,<br>consectetur adipiscing elit</div>
</div>

<div class="abs f-rule"></div>
<div class="abs social"><span></span><span></span><span></span><span></span></div>
<div class="abs copy">© 2021 Copyrights | Bright Lark Yard.com | All Rights Reserved</div>

</body>
</html>
```